International Automotive Parts Marketing business needs professional, sleek Android app design.

We have developed an Android app for our sales team and are now looking for an overall design our developers can apply. The design should mirror our corporate website kvrelo.com. There is a LOT of data the reps need to work through so not really any images other that login screen - of course icons are great. Lots of lists and searches etc. - it needs to look professional, feel amazing and easy to use. Our motto - Simple is always better. We included our logo and a few screenshots of the app page 1 and 2.

Target Market(s)

Professional Sales and Marketing - our own sales team (100 reps) will use this app

Font styles to use
Sans Serif

Colors

Designer to choose colors to be used in the design.

Requirements
Must have
• App design must be professional and easy to use in the field all day. Similar look and feel of corporate website kvrelo.com. Same colors and images. Icons to manage navigation
Should not have
• Non-professional look and feel. No vector cartoon type images. No specific parts related images

```html
<!DOCTYPE html>
<html lang="en">
<head>
<meta charset="utf-8">
<title>Search</title>
<link rel="stylesheet" href="https://fonts.googleapis.com/css2?family=Nunito:wght@400;600;700;800&display=swap">
<style>
  :root {
    --ink: #000000;
    --paper: #ffffff;
    --pill-dark: #1e1e1e;
    --accent-red: #b5122c;
    --muted: #9a9a9a;
    --label: #555555;
    --rule: #cfcfcf;
  }
  * { box-sizing: border-box; margin: 0; padding: 0; }
  html, body { width: 675px; height: 1200px; overflow: hidden; background: var(--paper); }
  body { font-family: "Nunito", sans-serif; position: relative; }

  .header {
    position: absolute; left: 0; top: 0; width: 675px; height: 537px;
    background: var(--ink); color: var(--paper);
  }
  .status-bar { position: absolute; left: 0; top: 0; width: 675px; height: 44px; }
  .status-time { position: absolute; left: 21px; top: 9px; font-size: 19px; font-weight: 600; letter-spacing: 0.3px; }
  .status-icons { position: absolute; right: 20px; top: 12px; }

  .menu-icon { position: absolute; left: 25px; top: 71px; }
  .title {
    position: absolute; left: 0; width: 675px; top: 64px; text-align: center;
    font-size: 33px; font-weight: 400; letter-spacing: 0.3px;
  }
  .search-icon { position: absolute; left: 621px; top: 67px; }

  .field {
    position: absolute; height: 62px; border: 2px solid var(--paper); border-radius: 31px;
    display: flex; align-items: center; font-size: 15px; color: var(--paper);
  }
  .field-type { left: 38px; top: 152px; width: 279px; padding-left: 28px; }
  .field-rating { left: 359px; top: 152px; width: 279px; padding-left: 31px; }
  .field-query { left: 38px; top: 244px; width: 599px; padding-left: 31px; }

  .btn {
    position: absolute; display: flex; align-items: center; justify-content: center;
    border-radius: 32px; font-size: 21px; font-weight: 800;
  }
  .btn-search { left: 38px; top: 337px; width: 599px; height: 64px; background: var(--paper); color: var(--accent-red); }
  .btn-tab { top: 428px; width: 279px; height: 64px; background: var(--pill-dark); color: var(--paper); }
  .btn-clients { left: 38px; }
  .btn-company { left: 359px; }

  .dropdown {
    position: absolute; left: 38px; top: 588px; width: 599px; height: 64px;
    border-radius: 32px; background: var(--paper);
    box-shadow: 0 2px 8px rgba(0,0,0,0.14);
    display: flex; align-items: center; padding-left: 38px;
    font-size: 18px; color: var(--muted);
  }
  .dropdown-caret { position: absolute; right: 26px; top: 28px; }

  .filter-list { position: absolute; left: 49px; top: 671px; width: 579px; list-style: none; }
  .filter-item {
    height: 60px; border-bottom: 1px solid var(--rule);
    display: flex; align-items: flex-end; padding-bottom: 14px;
    font-size: 15.5px; color: var(--label);
  }
  .filter-item:last-child { height: 64px; padding-bottom: 24px; }
</style>
</head>
<body>
  <header class="header">
    <div class="status-bar">
      <span class="status-time">9:41</span>
      <svg class="status-icons" width="96" height="18" viewBox="0 0 96 18">
        <rect x="0" y="11" width="3.5" height="5" rx="1" fill="#fff"/>
        <rect x="5.5" y="8" width="3.5" height="8" rx="1" fill="#fff"/>
        <rect x="11" y="5" width="3.5" height="11" rx="1" fill="#fff"/>
        <rect x="16.5" y="2" width="3.5" height="14" rx="1" fill="#fff"/>
        <path d="M28 6.5a13 13 0 0 1 18 0M31 9.8a8.5 8.5 0 0 1 12 0M34 13a4 4 0 0 1 6 0" stroke="#fff" stroke-width="2.2" fill="none" stroke-linecap="round"/>
        <circle cx="37" cy="15.5" r="1.6" fill="#fff"/>
        <rect x="57" y="2" width="33" height="14" rx="4" stroke="#fff" stroke-width="1.4" fill="none"/>
        <rect x="59.5" y="4.5" width="28" height="9" rx="2" fill="#fff"/>
        <rect x="91.5" y="6.5" width="2" height="5" rx="1" fill="#fff"/>
      </svg>
    </div>

    <svg class="menu-icon" width="29" height="28" viewBox="0 0 29 28" aria-label="Menu">
      <g fill="#fff">
        <rect x="0" y="0" width="7" height="7"/><rect x="11" y="0" width="7" height="7"/><rect x="22" y="0" width="7" height="7"/>
        <rect x="0" y="10.5" width="7" height="7"/><rect x="11" y="10.5" width="7" height="7"/><rect x="22" y="10.5" width="7" height="7"/>
        <rect x="0" y="21" width="7" height="7"/><rect x="11" y="21" width="7" height="7"/><rect x="22" y="21" width="7" height="7"/>
      </g>
    </svg>
    <h1 class="title">Search</h1>
    <svg class="search-icon" width="33" height="33" viewBox="0 0 33 33" aria-label="Search">
      <circle cx="13" cy="13" r="11" stroke="#fff" stroke-width="2" fill="none"/>
      <path d="M6.5 11a7 7 0 0 1 5-5" stroke="#fff" stroke-width="1.5" fill="none" stroke-linecap="round"/>
      <path d="M21 21l9.5 9.5" stroke="#fff" stroke-width="3.2" stroke-linecap="round"/>
    </svg>

    <div class="field field-type">Type</div>
    <div class="field field-rating">Rating</div>
    <div class="field field-query">Please Enter Here</div>

    <div class="btn btn-search">Search</div>
    <div class="btn btn-tab btn-clients">My Clients</div>
    <div class="btn btn-tab btn-company">My Company</div>
  </header>

  <div class="dropdown">
    More Option
    <svg class="dropdown-caret" width="16" height="9" viewBox="0 0 16 9"><path d="M0 0h16L8 9z" fill="#777"/></svg>
  </div>

  <ul class="filter-list">
    <li class="filter-item" style="height:56px">Market</li>
    <li class="filter-item">Franchise</li>
    <li class="filter-item">LOI</li>
    <li class="filter-item">Rewards</li>
    <li class="filter-item">Touch Start</li>
    <li class="filter-item">Touch End</li>
    <li class="filter-item">Sale Type</li>
  </ul>
</body>
</html>
```